TALL Harborin business card design

We had logo design for New Investment company "Tall Harbor" office in Vietnam, Singapore. We would like to design te card " less is more" simple, humble but give the receiver a strong attention and trust

Ex
Lam Duc Thien
Chairman

Address:
Hanoi Office
The Lotus Court, #B305. Kela road, Ward Phuan 2, District North Sonven. Hanoi
Hochiminh city office
Daravo Commerce Tower, Level 37th. #5 Lo Bang st. District 1. Hochiminh City
Singapore office:
14 Pembury Road #05-02 Pembury Point Singapore 239417

M. .......
E: thien.lam@tallharbor.com.vn
W: www.tallharbor.com

Target Market(s)

Startup, partner....

Industry/Entity Type

Investment

Contact Information for Business Card

Lam Duc Thien
Chairman

Address:
Hanoi Office
Hochiminh city office
Singapore office:
M. .......
W: www.tallharbor.com

Colors

Designer to choose colors to be used in the design.

Requirements
Must have
• Less is more. Simple Humble elegant
Nice to have
• Less color, 2 or 1.
• TALL may have color ,the rest may greyscale

```html
<!DOCTYPE html>
<html lang="en">
<head>
<meta charset="utf-8">
<title>Tall Harbor — Business Card</title>
<link href="https://fonts.googleapis.com/css2?family=Roboto+Condensed:wght@400;700&display=swap" rel="stylesheet">
<style>
  :root {
    --backdrop: #115a8c;
    --card-white: #ffffff;
    --brand-blue: #1570bd;
    --slate: #858689;
    --ink-grey: #77787b;
    --on-slate: #ffffff;
    --divider: #a4a5a8;
  }
  * { box-sizing: border-box; margin: 0; padding: 0; }
  html, body {
    width: 1200px; height: 1200px; overflow: hidden;
    background: var(--backdrop);
    font-family: "Roboto Condensed", Arial, sans-serif;
  }
  .card {
    position: absolute; left: 54px; top: 303px;
    width: 1091px; height: 594px;
    background: var(--card-white);
    overflow: hidden;
    box-shadow: 0 14px 40px rgba(0,0,0,0.45);
  }
  .card__bands { position: absolute; inset: 0; width: 100%; height: 100%; }
  .wordmark {
    position: absolute; left: 105px; top: 78px;
    font-weight: 700; font-size: 76px; line-height: 1;
    color: var(--brand-blue); letter-spacing: 1px;
  }
  .holder { position: absolute; left: 686px; top: 56px; }
  .holder__name {
    font-weight: 700; font-size: 54px; line-height: 1.1;
    color: var(--brand-blue);
  }
  .holder__title {
    font-size: 29px; color: var(--ink-grey); margin-top: 6px;
  }
  .offices {
    position: absolute; left: 105px; top: 300px;
    color: var(--on-slate);
  }
  .office__name { font-weight: 700; font-size: 29px; line-height: 34px; }
  .office__address { font-size: 23.5px; line-height: 30px; margin-bottom: 2px; }
  .divider {
    position: absolute; left: 656px; top: 295px;
    width: 2px; height: 263px; background: var(--divider);
  }
  .contacts {
    position: absolute; left: 674px; top: 338px;
    list-style: none; color: var(--on-slate);
  }
  .contact {
    display: flex; align-items: center; gap: 10px;
    font-size: 28px; height: 36px; margin-bottom: 24px;
  }
  .contact:nth-child(2) { margin-bottom: 26px; }
  .contact__icon { width: 32px; height: 32px; flex: none; }
  .contact__at { width: 32px; font-size: 34px; font-weight: 700; font-style: italic; text-align: center; }
</style>
</head>
<body>
  <div class="card">
    <svg class="card__bands" viewBox="0 0 1091 594" preserveAspectRatio="none" aria-hidden="true">
      <polygon points="0,255 1091,172 1091,180 0,310" fill="var(--brand-blue)"/>
      <polygon points="0,310 1091,180 1091,594 0,594" fill="var(--slate)"/>
    </svg>

    <div class="wordmark">TALL Harbor</div>

    <div class="holder">
      <div class="holder__name">Lam Duc Thien</div>
      <div class="holder__title">Chairman</div>
    </div>

    <div class="offices">
      <div class="office__name">Hanoi Office</div>
      <div class="office__address">The Lotus Court, #B305. Kela road,<br>Ward Phuan 2, District North Sonven. Hanoi</div>
      <div class="office__name">Hochiminh city office</div>
      <div class="office__address">Daravo Commerce Tower, Level 37th.<br>#5 Lo Bang st. District 1. Hochiminh City</div>
      <div class="office__name">Singapore office</div>
      <div class="office__address">14 Pembury Road #05-02 Pembury Point Singapore 239417</div>
    </div>

    <div class="divider"></div>

    <ul class="contacts">
      <li class="contact">
        <svg class="contact__icon" viewBox="0 0 32 32" aria-hidden="true">
          <path d="M9 3 L13 3 L14 9 L11 11 C12 16 15 21 19 24 L22 21 L27 24 L26 29 C16 29 7 17 7 6 Z" fill="none" stroke="#fff" stroke-width="2.2" stroke-linejoin="round"/>
        </svg>
        <span>123 555 0147</span>
      </li>
      <li class="contact">
        <span class="contact__at">@</span>
        <span>thien.lam@tallharbor.com.vn</span>
      </li>
      <li class="contact">
        <svg class="contact__icon" viewBox="0 0 32 32" aria-hidden="true">
          <g fill="none" stroke="#fff" stroke-width="1.6">
            <circle cx="16" cy="16" r="13"/>
            <ellipse cx="16" cy="16" rx="6" ry="13"/>
            <line x1="3" y1="16" x2="29" y2="16"/>
            <path d="M5 9 H27 M5 23 H27"/>
          </g>
        </svg>
        <span>tallharbor.com</span>
      </li>
    </ul>
  </div>
</body>
</html>
```